Q5 Pops (CBD candy infused with Delta-8)

The proposed logo are two pool table balls. One is a D and the other is an 8, its a brand and we need a label for Gummy human treats. This treats are being infused with Delt-8. I i will upload examples only. The example is of the type of labels needed (package and label for bottle)

Target Market(s)

Your professionals

Font styles to use
Sans Serif

Requirements
Must have
• Youthful look
Nice to have
• Consider using the Delta symbol instead of the D.
Also, I provided a sample of a label that's used on two type of packages.

```html
<!DOCTYPE html>
<html lang="en">
<head>
<meta charset="utf-8">
<title>Q5 Pops – Gummies Packaging Options</title>
<link rel="stylesheet" href="https://fonts.googleapis.com/css2?family=Arimo:wght@400&family=Barlow:wght@400;500;700;800&display=swap">
<style>
  :root {
    --backdrop: #e4e4e4;
    --pouch-black: #111111;
    --brand-red: #e10b14;
    --brand-red-deep: #b9060d;
    --ball-white: #f4f4f4;
    --ink: #111111;
    --paper: #ffffff;
    --soft-grey: #dcdcdc;
  }
  * { margin: 0; padding: 0; box-sizing: border-box; }
  html, body {
    width: 1200px;
    height: 842px;
    overflow: hidden;
    background: var(--backdrop);
  }
  .board {
    position: relative;
    width: 1200px;
    height: 842px;
  }
  .option-tab {
    position: absolute;
    top: 0;
    width: 311px;
    height: 59px;
    background: var(--ink);
    border-radius: 0 0 30px 30px;
    color: var(--paper);
    font-family: "Arimo", Arial, sans-serif;
    font-size: 38px;
    line-height: 59px;
    text-align: center;
    letter-spacing: 0.5px;
  }
  .option-tab--one { left: 201px; }
  .option-tab--two { left: 695px; }
  .pouch {
    position: absolute;
    top: 144px;
    width: 346px;
    height: 556px;
  }
  .pouch--one { left: 196px; }
  .pouch--two { left: 675px; }
  .pouch svg { display: block; }
  .tagline {
    font-family: "Barlow", sans-serif;
    font-weight: 400;
    font-size: 16.5px;
    fill: var(--paper);
    letter-spacing: 0.3px;
  }
  .strength {
    font-family: "Barlow", sans-serif;
    font-weight: 700;
    font-size: 47px;
    fill: var(--paper);
    letter-spacing: 0.5px;
  }
  .brand-name {
    font-family: "Barlow", sans-serif;
    font-weight: 800;
    font-size: 54px;
    fill: var(--brand-red);
  }
  .product-type {
    font-family: "Barlow", sans-serif;
    font-weight: 500;
    font-size: 15px;
    fill: var(--ink);
    letter-spacing: 0.6px;
  }
  .spec-label {
    font-family: "Barlow", sans-serif;
    font-weight: 700;
    font-size: 11px;
    fill: var(--paper);
  }
  .spec-value {
    font-family: "Barlow", sans-serif;
    font-weight: 700;
    font-size: 22px;
    fill: var(--soft-grey);
  }
</style>
</head>
<body>
<main class="board">

  <div class="option-tab option-tab--one">OPTION-1</div>
  <div class="option-tab option-tab--two">OPTION-2</div>

  <!-- Option 1 -->
  <section class="pouch pouch--one" aria-label="Option 1 pouch front">
    <svg width="346" height="556" viewBox="0 0 346 556">
      <defs>
        <clipPath id="pouch-shape-one"><rect x="0" y="0" width="346" height="556"/></clipPath>
      </defs>
      <g clip-path="url(#pouch-shape-one)">
        <rect class="pouch-body" x="0" y="0" width="346" height="556" fill="var(--pouch-black)"/>
        <circle class="red-disc" cx="173" cy="258" r="224" fill="var(--brand-red)"/>
        <circle class="emblem-ring" cx="173" cy="78" r="24" fill="none" stroke="var(--ink)" stroke-width="1.5"/>
        <circle class="ball-face" cx="173" cy="252" r="124" fill="var(--ball-white)"/>
        <text class="brand-name" x="173" y="250" text-anchor="middle">Q5 Pops</text>
        <text class="product-type" x="173" y="284" text-anchor="middle">GUMMIES</text>
        <text class="tagline" x="173" y="413" text-anchor="middle">CBD candy infused with</text>
        <text class="strength" x="165" y="459" text-anchor="middle">DELTA-8</text>
        <text class="spec-label" x="48" y="526">NET WT.</text>
        <text class="spec-value" x="97" y="526">40g</text>
        <text class="spec-value" x="227" y="526">30<tspan font-size="13">mg CBD</tspan></text>
      </g>
    </svg>
  </section>

  <!-- Option 2 -->
  <section class="pouch pouch--two" aria-label="Option 2 pouch front">
    <svg width="346" height="556" viewBox="0 0 346 556">
      <defs>
        <clipPath id="pouch-shape-two"><rect x="0" y="0" width="346" height="556"/></clipPath>
      </defs>
      <g clip-path="url(#pouch-shape-two)">
        <rect class="pouch-body" x="0" y="0" width="346" height="556" fill="var(--pouch-black)"/>
        <circle class="red-disc" cx="173" cy="262" r="224" fill="var(--brand-red)"/>
        <circle class="emblem-ring" cx="173" cy="78" r="24" fill="none" stroke="var(--ink)" stroke-width="1.5"/>
        <circle class="ball-face" cx="173" cy="268" r="123" fill="var(--ball-white)"/>
        <text class="brand-name" x="173" y="268" text-anchor="middle">Q5 Pops</text>
        <text class="product-type" x="173" y="302" text-anchor="middle">GUMMIES</text>
        <text class="tagline" x="173" y="417" text-anchor="middle">CBD candy infused with</text>
        <text class="strength" x="165" y="463" text-anchor="middle">DELTA-8</text>
        <text class="spec-label" x="48" y="530">NET WT.</text>
        <text class="spec-value" x="97" y="530">40g</text>
        <text class="spec-value" x="227" y="530">30<tspan font-size="13">mg CBD</tspan></text>
      </g>
    </svg>
  </section>

</main>
</body>
</html>
```